Jewelry Shop Needs a Business Card Design

***We want a very sharp and unforgettable pantone for the Business Card. ***
***We do not want the business card or logo only in black, white and grey color!!!Please provide us a main color as our brand topic! Thanks!! ***

Mabel’s Nook is a Hong Kong based fine jewelry brand.

We want a very nice, simple and elegant business card design for Mabel's Nook Brand. The company's logo has been uploaded already.

You can design with below info:

Dorian Fung
Director
M: +852 94273658
T: +852 35820417
F: +852 35820419
E: dorian.fung@mabelsnook.example
5/F , Harbourlight Tower, 12-18 Orchid Lane, Wan Tung Kok, Kowloon, Hong Kong

Target Market(s)

Mabel’s Nook philosophy is a jewelry icon of young, creative, trendy, fashionable, stylish, energetic, and elegant. For Mabel’s Nook, jewelry is one collection of artworks, the most important items in personal life.

Industry/Entity Type

Jewelry

Requirements
Must have
• We want a very sharp and unforgettable pantone for the Business Card.

```html
<!DOCTYPE html>
<html lang="en">
<head>
<meta charset="utf-8">
<title>Mabel’s Nook — Business Card</title>
<link rel="stylesheet" href="https://fonts.googleapis.com/css2?family=Cinzel:wght@500;600;700&family=Lato:wght@400;700&display=swap">
<style>
  :root {
    --brand: #a3124a;
    --brand-deep: #7d0d39;
    --paper: #ffffff;
    --backdrop: #d9d9d9;
    --ink: #141414;
  }
  * { margin: 0; padding: 0; box-sizing: border-box; }
  html, body { width: 1200px; height: 1000px; overflow: hidden; }
  body { background: var(--backdrop); position: relative; font-family: "Lato", sans-serif; }

  .card { position: absolute; }
  .card--front { left: 81px; top: 78px; width: 487px; height: 832px; background: var(--brand); }
  .card--back { left: 613px; top: 122px; width: 489px; height: 836px; background: var(--paper); }

  .brand-disc { position: absolute; border-radius: 50%; }
  .card--front .brand-disc { width: 222px; height: 222px; left: 132px; top: 236px; background: var(--paper); }
  .card--back .brand-disc { width: 224px; height: 224px; left: 131px; top: 51px; background: var(--brand); }

  .brand-name {
    position: absolute; left: 0; width: 100%; text-align: center;
    font-family: "Cinzel", serif; font-weight: 600; font-size: 40px; letter-spacing: 2px; line-height: 1;
  }
  .card--front .brand-name { top: 488px; color: var(--paper); }
  .card--back .brand-name { top: 304px; color: var(--brand); }

  .person { position: absolute; top: 408px; left: 0; width: 100%; text-align: center; font-family: "Cinzel", serif; font-weight: 700; }
  .person__name { font-size: 35px; letter-spacing: 1px; line-height: 40px; color: var(--ink); }
  .person__title { font-size: 22px; letter-spacing: 1px; line-height: 28px; color: var(--brand-deep); }

  .contact { position: absolute; top: 536px; left: 0; width: 100%; text-align: center; list-style: none; font-size: 20px; line-height: 29px; color: var(--ink); letter-spacing: 0.3px; }
  .contact b { font-weight: 700; color: var(--brand); }

  .address { position: absolute; top: 705px; left: 0; width: 100%; text-align: center; font-style: normal; font-weight: 700; font-size: 20px; line-height: 29px; color: var(--ink); }
</style>
</head>
<body>
  <section class="card card--front" aria-label="Card front">
    <div class="brand-disc"></div>
    <p class="brand-name">Mabel’s Nook</p>
  </section>

  <section class="card card--back" aria-label="Card back">
    <div class="brand-disc"></div>
    <p class="brand-name">Mabel’s Nook</p>
    <div class="person">
      <h1 class="person__name">DORIAN FUNG</h1>
      <p class="person__title">Director</p>
    </div>
    <ul class="contact">
      <li><b>M:</b> +852 94273658</li>
      <li><b>T:</b> +852 35820417</li>
      <li><b>F:</b> +852 35820419</li>
      <li><b>E:</b> dorian.fung@mabelsnook.example</li>
    </ul>
    <address class="address">
      5/F , Harbourlight Tower, 12-18<br>
      Orchid Lane, Wan Tung Kok, Kowloon,<br>
      Hong Kong.
    </address>
  </section>
</body>
</html>
```